Halvercroft Lending Group Loan Officer

I am looking for an upscale business card design with my company logo. I would love to have my picture, QR application code, and NMLS number along with the rest of my contacts information. I am a loan officer for a lending company. I want a card that stands, looks profession, upscale. First looks are everything. It would be nice to incorporate out colors and not just have a white card.

```html
<!DOCTYPE html>
<html lang="en">
<head>
<meta charset="utf-8">
<title>Halvercroft Lending Group – Business Card</title>
<link href="https://fonts.googleapis.com/css2?family=Jost:wght@400;500;600&display=swap" rel="stylesheet">
<style>
  :root {
    --backdrop: #8e8e8e;
    --card-white: #f7f7f6;
    --brand-blue: #0a4c9c;
    --brand-navy: #0a1f5c;
    --brand-sky: #22b2ee;
    --text-gray: #4a4a4a;
    --portrait-warm: #c9a27a;
    --portrait-dark: #2b3140;
  }
  * { box-sizing: border-box; margin: 0; padding: 0; }
  html, body { width: 1200px; height: 1200px; overflow: hidden; }
  body {
    background: var(--backdrop);
    font-family: "Jost", "Futura", sans-serif;
    position: relative;
  }
  .card {
    position: absolute;
    left: 262px;
    width: 686px;
    height: 391px;
    overflow: hidden;
  }
  .card-front { top: 165px; background: var(--card-white); }
  .card-back  { top: 653px; background: var(--brand-blue); }

  .brand {
    position: absolute; left: 54px; top: 36px;
    display: flex; align-items: center; gap: 12px;
  }
  .brand-square { width: 40px; height: 40px; background: var(--brand-blue); }
  .brand-name {
    color: var(--brand-blue); font-weight: 500;
    font-size: 21px; line-height: 23px; letter-spacing: 0.5px;
  }

  .holder-name {
    position: absolute; left: 50px; top: 148px;
    color: var(--brand-blue); font-weight: 600; font-size: 23px; letter-spacing: 0.2px;
  }
  .holder-title {
    position: absolute; left: 50px; top: 175px;
    color: var(--text-gray); font-size: 16px;
  }
  .address {
    position: absolute; left: 50px; top: 205px;
    color: var(--text-gray); font-size: 16px; line-height: 19px;
  }
  .contacts {
    position: absolute; left: 50px; top: 256px; list-style: none;
    color: var(--text-gray); font-size: 16px; line-height: 19.5px;
  }
  .contacts li { display: flex; align-items: center; gap: 10px; }
  .contacts svg { width: 14px; height: 14px; fill: var(--brand-blue); flex: none; }
  .nmls {
    position: absolute; left: 52px; top: 345px;
    color: var(--text-gray); font-size: 16px;
  }
  .portrait {
    position: absolute; left: 313px; top: 20px; right: 0; bottom: 0;
    background: radial-gradient(ellipse at 55% 35%, var(--portrait-warm) 0%, #b58a62 40%, var(--portrait-dark) 85%);
    border-radius: 160px 160px 0 0;
  }
  .pattern-field {
    position: absolute; inset: 0;
    background: linear-gradient(90deg, var(--brand-sky) 0%, #1b7fd0 30%, #0e4e9e 50%, #0b2f78 75%, var(--brand-navy) 100%);
  }
</style>
</head>
<body>
  <section class="card card-front">
    <div class="brand">
      <span class="brand-square"></span>
      <span class="brand-name">HALVERCROFT<br>LENDING GROUP</span>
    </div>
    <h1 class="holder-name">DANIEL WHITMORE</h1>
    <p class="holder-title">Founder &amp; CEO</p>
    <p class="address">4120 Larchmont Way<br>Juneau, Alaska 34590</p>
    <ul class="contacts">
      <li><svg viewBox="0 0 24 24"><path d="M6.6 10.8a15 15 0 0 0 6.6 6.6l2.2-2.2a1 1 0 0 1 1-.25 11.4 11.4 0 0 0 3.6.57 1 1 0 0 1 1 1V20a1 1 0 0 1-1 1A17 17 0 0 1 3 4a1 1 0 0 1 1-1h3.5a1 1 0 0 1 1 1c0 1.25.2 2.45.57 3.57a1 1 0 0 1-.25 1z"/></svg>555-210-4831</li>
      <li><svg viewBox="0 0 24 24"><path d="M7 1h10a2 2 0 0 1 2 2v18a2 2 0 0 1-2 2H7a2 2 0 0 1-2-2V3a2 2 0 0 1 2-2zm0 3v15h10V4z"/></svg>555-210-7729</li>
      <li><svg viewBox="0 0 24 24"><path d="M2 5h20v14H2zm2 2v.5l8 5 8-5V7l-8 5z"/></svg>info@halvercroftlg.com</li>
      <li><svg viewBox="0 0 24 24"><circle cx="12" cy="12" r="10"/></svg>www.halvercroftlg.com</li>
    </ul>
    <p class="nmls">NMLS #48213</p>
    <div class="portrait" role="img" aria-label="Portrait photo of the loan officer"></div>
  </section>

  <section class="card card-back">
    <div class="pattern-field" role="img" aria-label="Repeating brand pattern fading from sky blue to navy"></div>
  </section>
</body>
</html>
```